wine lables

Waimoa Kilvane Spa Resort is a Thermal Holiday Park and Resort, Hot Pools and Day Spa in beautiful Taupo New Zealand. We place NZ wines in our accomodation rooms when people are stayin at our resort. We need a new, comtemporary design for our wine labels to represent the beauty of our region and resort. For more information on our resort go wo www.waimoakilvane.co.nz

Target Market(s)

Travellers wanting to relax. Nature and wine lovers

Requirements
Must have
• must have out logo somewhere
must have copy that is seen on the attached current wine label.
Need one for each of the wine types listed in the attachments

```html
<!DOCTYPE html>
<html lang="en">
<head>
<meta charset="utf-8">
<title>Waimoa Kilvane – Wine Labels</title>
<link rel="stylesheet" href="https://fonts.googleapis.com/css2?family=Source+Sans+3:wght@400;600;700&family=Tinos&display=swap">
<style>
  :root {
    --page: #ffffff;
    --leaf: #8cc63f;
    --olive: #4a5a1a;
    --ink: #111111;
    --band: #1a1a1a;
    --paper: #ffffff;
  }
  * { margin: 0; padding: 0; box-sizing: border-box; }
  html, body { width: 1200px; height: 1026px; overflow: hidden; background: var(--page); }
  .sheet { position: relative; width: 1200px; height: 1026px; font-family: "Source Sans 3", sans-serif; color: var(--ink); }
  .shapes { position: absolute; inset: 0; }
  .brand { position: absolute; left: 120px; width: 400px; text-align: center; }
  .brand-name { top: 322px; font-size: 28px; font-weight: 700; letter-spacing: -0.3px; }
  .brand-tagline { top: 360px; font-size: 13.5px; letter-spacing: 2.4px; font-weight: 400; }
  .varietal {
    position: absolute; left: 132px; top: 596px; width: 348px;
    font-family: "Tinos", serif; color: var(--paper);
    font-size: 30px; line-height: 36px; text-align: center;
  }
  .story {
    position: absolute; left: 646px; top: 302px; width: 400px;
    font-size: 18.5px; line-height: 25.4px; font-weight: 600; text-align: center;
  }
  .legal {
    position: absolute; left: 703px; top: 588px; width: 330px;
    font-size: 13px; line-height: 16.5px; font-weight: 600;
  }
  .volume {
    position: absolute; left: 703px; top: 697px;
    font-size: 13px; line-height: 16.5px; font-weight: 600;
  }
</style>
</head>
<body>
<main class="sheet">
  <svg class="shapes" width="1200" height="1026" viewBox="0 0 1200 1026" aria-hidden="true">
    <defs>
      <filter id="label-shadow" x="-20%" y="-20%" width="140%" height="140%">
        <feDropShadow dx="6" dy="8" stdDeviation="7" flood-color="#000" flood-opacity="0.35"/>
      </filter>
      <linearGradient id="window-tone" x1="0" y1="0" x2="1" y2="0">
        <stop offset="0" stop-color="#ffffff"/>
        <stop offset="0.55" stop-color="#ffffff"/>
        <stop offset="1" stop-color="#9aa57a"/>
      </linearGradient>
    </defs>
    <!-- front label -->
    <ellipse class="front-rim" cx="307" cy="528" rx="225" ry="334" fill="var(--paper)" filter="url(#label-shadow)"/>
    <ellipse class="front-field" cx="307" cy="525" rx="203" ry="307" fill="var(--leaf)"/>
    <circle class="brand-mark" cx="320" cy="284" r="27" fill="var(--ink)"/>
    <rect class="varietal-band" x="132" y="580" width="348" height="106" rx="26" fill="var(--band)"/>
    <!-- back label -->
    <ellipse class="back-field" cx="896" cy="525" rx="236" ry="315" fill="var(--leaf)"/>
    <g class="compliance-icons" fill="none" stroke="var(--paper)" stroke-width="2.5">
      <circle cx="825" cy="722" r="15"/>
      <circle cx="877" cy="722" r="17"/>
      <circle cx="928" cy="720" r="14"/>
    </g>
  </svg>

  <svg class="shapes" width="1200" height="1026" viewBox="0 0 1200 1026" role="img" aria-label="Decorative window with swirl motif">
    <ellipse class="front-window" cx="350" cy="603" rx="143" ry="207" fill="url(#window-tone)"/>
    <rect x="132" y="580" width="348" height="106" rx="26" fill="var(--band)"/>
  </svg>

  <div class="brand brand-name">Waimoa Kilvane</div>
  <div class="brand brand-tagline">STAY - SOAK - SOOTHE - SAVOUR</div>
  <div class="varietal">CABERNET<br>SAUVIGNON MERLOT</div>

  <p class="story">The Waimoa Kilvane Range of<br>wines are styled for enjoyment<br>upon releace, and have been<br>crafted with the discerning palates<br>of our patrons in mind, and easy<br>drinking wine that accompanies many<br>contemporary food styles, where the<br>fresh wholesome flavours of the<br>ingredients are allowed to shine.</p>

  <p class="legal">Produced by Harbourline Brands Ltd.<br>14 Kereru Lane Ruawai<br>www.harbourlinebrands.co.nz<br>Produced with the aid of fish, milk and egg<br>products and traces may remain.<br>Contains preservatives (220) added.</p>

  <p class="volume">e 750 ML<br>13.0% Alc/Vol</p>
</main>
</body>
</html>
```